Needed Box Packaging: Dog XL Puppy Pee/Poo Pads

We're looking for a creative and fun design for our XL puppy pads. Attached is all the documents you will need.

Our pads are unique with Bamboo Charcoal and optional Adhesive sticker backing on the corners. 23" x 35" is the size. There's 50 per box.

ABSORBS 2x as much, 2x as fast, so you never come home to ruined floors
BLACK puppy pads, so your pets mess stays discrete and you never see a yellow stain on a white puppy pad in your home
ODOR ELIMINATION with carbon technology for all-day use to ensure your home stays fresh
LEAK PROOF Sorbix Polymer turns liquid into gel instantly to guarantee dry floors and easy clean up
PHEROMONE ATTRACTION to ensure pets feel comfortable and knows to hit the right spot every time

Target Market(s)

Dog owners

Font styles to use
Sans Serif

Colors
33a6d7
33b8a4
acd036
fbee3d
faa54b

Requirements
Must have
• Must have logo, size of pads, benefits, UPC code, number packed per box, pictures of a dog and picture of the pads
Should not have
• cats

```html
<!DOCTYPE html>
<html lang="en">
<head>
<meta charset="utf-8">
<title>Puppy Training Pads – Box Front</title>
<link rel="stylesheet" href="https://fonts.googleapis.com/css2?family=Bitter:wght@700;800;900&family=Fira+Sans+Condensed:wght@400;700&family=Fira+Sans:wght@800&display=swap">
<style>
  :root {
    --sky: #3fb1e3;
    --white: #ffffff;
    --ink: #111111;
    --blue: #2f74b5;
    --green: #acd036;
    --orange: #faa54b;
    --yellow: #f4ea3f;
    --teal: #2cb8a0;
    --gold: #f7bd18;
    --floor-light: #c79a6d;
    --floor-dark: #8b5e3c;
  }
  html, body {
    margin: 0;
    width: 1055px;
    height: 1200px;
    overflow: hidden;
    background: var(--sky);
  }
  .box-front {
    position: absolute;
    left: 138px;
    top: 94px;
    width: 782px;
    height: 1017px;
    background: radial-gradient(circle at 85% 20%, #eef4da 0, transparent 45%),
                radial-gradient(circle at 10% 45%, #e3eef8 0, transparent 40%),
                var(--white);
    overflow: hidden;
  }
  .floor-photo {
    position: absolute;
    left: 0; top: 678px;
    width: 782px; height: 244px;
    background: linear-gradient(180deg, var(--floor-light), var(--floor-dark));
  }
  .dog-photo {
    position: absolute;
    left: 414px; top: 130px;
    width: 368px; height: 790px;
    background: linear-gradient(160deg, #5a4335 0%, #3a2c24 40%, #e9e4df 70%, #2d2d2d 100%);
    border-radius: 160px 120px 0 0;
  }
  .brand {
    position: absolute;
    right: 24px; top: 36px;
    font-family: "Fira Sans", sans-serif;
    font-weight: 800;
    font-size: 32px;
    color: var(--ink);
    margin: 0;
  }
  .title {
    position: absolute;
    left: 50px; top: 106px;
    margin: 0;
    font-family: "Bitter", serif;
    line-height: 1;
  }
  .title .big {
    display: block;
    font-size: 108px;
    font-weight: 900;
    color: var(--ink);
    letter-spacing: 1px;
  }
  .title .sub {
    display: block;
    margin-top: 4px;
    font-size: 43px;
    font-weight: 700;
  }
  .sub .g { color: var(--green); }
  .sub .o { color: var(--orange); }
  .benefits { list-style: none; margin: 0; padding: 0; }
  .benefit {
    position: absolute;
    left: 69px;
    width: 315px;
    height: 52px;
    border-radius: 4px;
    color: var(--white);
    font-family: "Fira Sans Condensed", sans-serif;
    padding: 6px 26px 0 33px;
    box-sizing: border-box;
  }
  .benefit::before, .benefit::after {
    content: "";
    position: absolute;
    width: 30px; height: 30px;
    border-radius: 50%;
    background: inherit;
    border: 4px solid var(--white);
  }
  .benefit::before { left: -26px; top: -20px; }
  .benefit::after { right: -26px; bottom: -18px; }
  .benefit strong { display: block; font-size: 18px; line-height: 1.1; }
  .benefit span { display: block; font-size: 10px; line-height: 1.25; }
  .b1 { top: 341px; background: var(--blue); }
  .b2 { top: 431px; background: var(--green); }
  .b3 { top: 520px; background: var(--orange); }
  .b4 { top: 608px; background: var(--yellow); }
  .b5 { top: 696px; background: var(--teal); }
  .bottom-band {
    position: absolute;
    left: 0; top: 920px;
    width: 782px; height: 97px;
    background: var(--gold);
  }
  .count-badge {
    position: absolute;
    left: 32px; top: 842px;
    width: 150px; height: 175px;
    border-radius: 75px 75px 0 0;
    background: var(--gold);
    color: var(--white);
    text-align: center;
    font-family: "Bitter", serif;
  }
  .count-badge .num {
    display: block;
    font-family: "Fira Sans", sans-serif;
    font-weight: 800;
    font-size: 88px;
    line-height: 1;
    margin-top: 12px;
  }
  .count-badge .pcs { display: block; font-size: 26px; font-weight: 700; line-height: 1; }
  .count-badge .size { display: block; font-size: 20px; font-weight: 700; line-height: 1; }
  .features {
    position: absolute;
    left: 194px; top: 938px;
    margin: 0;
    font-family: "Bitter", serif;
    font-weight: 700;
    font-size: 29px;
    line-height: 1.15;
    color: var(--white);
  }
</style>
</head>
<body>
  <main class="box-front">
    <div class="floor-photo" role="img" aria-label="Wooden floor with a black training pad laid on it"></div>
    <div class="dog-photo" role="img" aria-label="Brindle and white boxer puppy sitting on a black training pad"></div>

    <p class="brand">Pawtrail</p>

    <h1 class="title">
      <span class="big">PUPPY</span>
      <span class="sub"><span class="g">TRAINING</span> <span class="o">PADS</span></span>
    </h1>

    <ul class="benefits">
      <li class="benefit b1"><strong>ABSORBS 2x as much, 2x as fast,</strong><span>so you never come home to ruined floors</span></li>
      <li class="benefit b2"><strong>BLACK puppy pads</strong><span>so your pets mess stays discrete and you never see a yellow stain on a white puppy pad in your home</span></li>
      <li class="benefit b3"><strong>ODOR ELIMINATION</strong><span>with carbon technology for all-day use to ensure your home stays fresh</span></li>
      <li class="benefit b4"><strong>LEAK PROOF</strong><span>Sorbix Polymer turns liquid into gel instantly to guarantee dry floors and easy clean up</span></li>
      <li class="benefit b5"><strong>PHEROMONE ATTRACTION</strong><span>to ensure pets feel comfortable and knows to hit the right spot every time</span></li>
    </ul>

    <div class="bottom-band"></div>
    <div class="count-badge">
      <span class="num">50</span>
      <span class="pcs">PIECES</span>
      <span class="size">23” x 35”</span>
    </div>
    <p class="features">Bamboo Charcoal and Optional<br>Adhesive sticker backing on the corners</p>
  </main>
</body>
</html>
```